Cosmetic Surgery Amberlane

I need a web design for a Cosmetic Surgery Clinic. The current site is cosmetic-surgery-amberlane.co.uk. The design should be:
- Flat Design with big banner
- Warm colors
- Responsive Layout
- SEO friendly

Industry/Entity Type

Cosmetic

```html
<!DOCTYPE html>
<html lang="en">
<head>
<meta charset="utf-8">
<title>Cosmetic Surgery Amberlane</title>
<link rel="stylesheet" href="https://fonts.googleapis.com/css2?family=Dosis:wght@400;500;600;700&family=Open+Sans:wght@400;600&display=swap">
<style>
:root{
  --pink:#c5125e;
  --pink-dark:#b00c52;
  --pink-soft:#c84b97;
  --ink:#333;
  --muted:#555;
  --line:#e3e3e3;
  --pale:#f4f4f4;
  --white:#fff;
}
*{margin:0;padding:0;box-sizing:border-box}
html,body{width:1200px;height:2862px;overflow:hidden}
body{position:relative;background:var(--white);font-family:"Open Sans",Arial,sans-serif;color:var(--ink)}
.abs{position:absolute}
.heading{font-family:"Dosis",Arial,sans-serif}
.photo{position:absolute}

/* hero */
.hero{left:0;top:0;width:1200px;height:719px;background:linear-gradient(100deg,#8fa0b4 0%,#b6c2cf 35%,#e6c9b8 62%,#f3e8e2 80%,#d9dce2 100%)}
.header{left:99px;top:0;width:1000px;height:118px;background:var(--white);box-shadow:0 2px 4px rgba(0,0,0,.08)}
.brand{left:35px;top:26px;display:flex;align-items:center;gap:10px}
.brand-dot{width:30px;height:30px;border-radius:50%;background:var(--pink)}
.brand-name{font-family:"Dosis",sans-serif;font-weight:600;font-size:26px;color:var(--pink);line-height:1.1;width:190px}
.nav{left:363px;top:46px;display:flex;font-family:"Dosis",sans-serif;font-size:17px;color:#444}
.nav a{color:inherit;text-decoration:none;position:absolute;white-space:nowrap;top:0;line-height:29px}
.nav .active{color:var(--pink);border:1.5px solid var(--pink);border-radius:3px;padding:0 15px;line-height:26px}
.hero-kicker{left:99px;top:292px;font-family:"Dosis",sans-serif;font-weight:500;font-size:50px;color:var(--white)}
.hero-title{left:99px;top:356px;font-family:"Dosis",sans-serif;font-weight:700;font-size:52px;color:var(--white);letter-spacing:.5px}
.btn-hero{left:99px;top:437px;width:178px;height:48px;background:var(--pink);color:var(--white);font-family:"Dosis",sans-serif;font-weight:600;font-size:18px;display:flex;align-items:center;justify-content:center;border-radius:2px}
.arrow{top:510px;width:34px;height:34px;border-radius:50%;background:rgba(80,80,80,.75)}

/* appointment bar */
.appt{left:99px;top:647px;width:1000px;height:93px;background:#eeeeee;box-shadow:0 2px 4px rgba(0,0,0,.12)}
.appt-label{left:29px;top:31px;font-family:"Dosis",sans-serif;font-weight:600;font-size:21px;color:var(--pink)}
.field{top:30px;height:37px;background:var(--white);border:1px solid #ddd;font-size:10px;color:#555;padding:0 10px;display:flex;align-items:center;justify-content:space-between}
.btn-next{left:861px;top:30px;width:114px;height:37px;background:var(--pink);color:var(--white);font-family:"Dosis",sans-serif;font-size:16px;font-weight:600;display:flex;align-items:center;justify-content:center}

/* welcome band */
.welcome{left:0;top:740px;width:1200px;height:174px;background:var(--pink-dark);color:var(--white);text-align:center}
.welcome h1{font-family:"Dosis",sans-serif;font-weight:500;font-size:30px;margin-top:28px}
.welcome p{width:960px;margin:18px auto 0;font-size:11px;line-height:21px}

/* services */
.service{top:965px;width:313px;text-align:center}
.service .thumb{width:313px;height:184px;background:linear-gradient(135deg,#e9d6cb,#c9b2a4 55%,#9ea6b0)}
.plus{position:absolute;left:136px;top:162px;width:42px;height:42px;border-radius:50%;background:var(--pink);border:3px solid var(--white)}
.service h3{font-family:"Dosis",sans-serif;font-weight:500;font-size:17px;color:#333;margin-top:34px}
.service p{font-size:11px;line-height:21px;color:#555;margin:10px auto 0;width:300px}
.btn-more{display:inline-flex;align-items:center;justify-content:center;height:32px;background:#e8e8e8;border:1px solid #d7d7d7;font-family:"Dosis",sans-serif;font-size:13px;color:#444;padding:0 18px;border-radius:2px}
.service .btn-more{margin-top:20px;width:103px}

/* holiday */
.holiday{left:0;top:1378px;width:1200px;height:374px;background:linear-gradient(90deg,#f5f3f4 0%,#faf6f7 50%,#f1eeef 100%)}
.holiday h2{position:absolute;left:99px;top:38px;font-family:"Dosis",sans-serif;font-weight:500;font-size:34px;color:var(--pink)}
.holiday h3{position:absolute;left:99px;top:84px;font-family:"Dosis",sans-serif;font-weight:500;font-size:22px;color:var(--pink)}
.holiday p{position:absolute;left:99px;top:120px;width:545px;font-size:12.5px;line-height:21.6px;color:#444}
.form{left:672px;top:1440px;width:429px;height:273px;background:var(--white);border:1px solid #e2e2e2}
.input{position:absolute;left:25px;width:381px;height:46px;border:1px solid #ddd;font-size:12px;color:#555;padding-left:16px;display:flex;align-items:center}
.input.focus{border-color:var(--pink)}
.btn-send{position:absolute;left:25px;top:200px;width:381px;height:48px;background:var(--pink);color:var(--white);font-family:"Dosis",sans-serif;font-size:20px;font-weight:500;display:flex;align-items:center;justify-content:center}

/* blog */
.section-title{font-family:"Dosis",sans-serif;font-weight:500;font-size:20px;color:var(--pink)}
.post-thumb{left:99px;width:229px;height:164px;background:linear-gradient(135deg,#2b2b2b,#8a7467 60%,#d9c3b6)}
.post{left:353px;width:410px}
.post h4{font-family:"Dosis",sans-serif;font-weight:500;font-size:17px;color:#333}
.post .date{font-family:"Dosis",sans-serif;font-weight:500;font-size:15px;color:var(--pink);margin-top:14px}
.post p{font-size:11px;line-height:19.5px;color:#555;margin-top:8px}
.post .btn-more,.ba .btn-more{margin-top:14px;padding:0 17px}
.ba{left:809px;width:292px}
.ba h4{font-family:"Dosis",sans-serif;font-weight:500;font-size:15px;color:#333;margin-top:23px}
.ba p{font-size:11px;line-height:19.5px;color:#555;margin-top:10px}
.rule{left:99px;top:2242px;width:1002px;height:1px;background:var(--line)}

/* testimonials */
.t-title{left:99px;top:2278px;font-family:"Dosis",sans-serif;font-weight:600;font-size:17px;color:#333}
.avatar{width:120px;height:120px;border-radius:50%;background:radial-gradient(circle at 50% 40%,#e7cdbd,#b58f79 70%,#7b6657)}
.quote{width:330px;font-size:11px;line-height:19.5px;color:#444}
.quote .mark{font-family:Georgia,serif;font-size:22px;color:#777;line-height:0;vertical-align:-6px;margin-right:4px}
.quote .who{margin-top:10px;font-size:11px}
.quote .who b{color:var(--pink);font-weight:600}

/* contact band */
.contact{left:0;top:2505px;width:1200px;height:107px;background:var(--pink-soft);color:var(--white)}
.icon-ring{position:absolute;top:35px;width:38px;height:38px;border-radius:50%;border:2px solid var(--white)}
.contact .info{position:absolute;top:28px;font-size:15px;line-height:27px}
.btn-quick{position:absolute;left:941px;top:35px;width:160px;height:43px;background:#f2f2f2;border-radius:3px;color:#444;font-family:"Dosis",sans-serif;font-size:16px;font-weight:500;display:flex;align-items:center;justify-content:center}

/* footer */
.footer{left:0;top:2612px;width:1200px;height:250px;background:#f3f3f3}
.f-title{position:absolute;top:28px;font-family:"Open Sans",sans-serif;font-weight:600;font-size:14px;color:var(--pink)}
.f-sub{position:absolute;left:99px;top:58px;font-size:11px;color:#444}
.f-list{position:absolute;list-style:none;font-size:11px;color:#444}
.f-list li{height:29px;padding-left:22px;position:relative}
.f-list li::before{content:"";position:absolute;left:2px;top:5px;width:5px;height:5px;border-top:1.5px solid var(--pink);border-right:1.5px solid var(--pink);transform:rotate(45deg)}
.social{position:absolute;top:67px;width:32px;height:32px;background:var(--pink-soft);border-radius:2px}
.news-input{position:absolute;left:845px;top:63px;width:181px;height:32px;background:var(--white);border:1px solid #ddd}
.btn-sub{position:absolute;left:1026px;top:63px;width:75px;height:32px;background:var(--pink-soft);color:var(--white);font-size:9px;font-weight:600;display:flex;align-items:center;justify-content:center}
.copy{position:absolute;left:0;width:1200px;top:210px;text-align:center;font-size:11px;color:#444}
</style>
</head>
<body>

<!-- hero -->
<div class="photo hero abs" role="img" aria-label="Woman lying back with eyes closed while a gloved hand marks her face for a facelift procedure"></div>

<header class="header abs">
  <div class="brand abs"><span class="brand-dot"></span><span class="brand-name">Cosmetic Surgery Amberlane</span></div>
  <nav class="nav abs">
    <a class="active" style="left:0;top:1px">Home</a>
    <a style="left:97px">About Us</a>
    <a style="left:189px">Services</a>
    <a style="left:277px">Appointment</a>
    <a style="left:397px">Blog</a>
    <a style="left:460px">Testimonials</a>
    <a style="left:567px">Contact</a>
  </nav>
</header>

<div class="hero-kicker abs">Face, Body, Breast</div>
<div class="hero-title abs">PLASTIC SURGERY</div>
<div class="btn-hero abs">Book an Appointment</div>
<div class="arrow abs" style="left:99px">
  <svg width="34" height="34" viewBox="0 0 34 34"><path d="M19 11 L13 17 L19 23" fill="none" stroke="#fff" stroke-width="2.5"/></svg>
</div>
<div class="arrow abs" style="left:141px">
  <svg width="34" height="34" viewBox="0 0 34 34"><path d="M15 11 L21 17 L15 23" fill="none" stroke="#fff" stroke-width="2.5"/></svg>
</div>

<!-- appointment bar -->
<div class="appt abs">
  <div class="appt-label abs">MAKE AN APPOINTMENT</div>
  <div class="field abs" style="left:258px;width:177px">Appointment date
    <svg width="12" height="12" viewBox="0 0 12 12"><rect x="1" y="2" width="10" height="9" fill="none" stroke="#c5125e" stroke-width="1.3"/><path d="M1 5h10" stroke="#c5125e" stroke-width="1.3"/></svg></div>
  <div class="field abs" style="left:452px;width:178px">Approximate Time
    <svg width="12" height="12" viewBox="0 0 12 12"><circle cx="6" cy="6" r="5" fill="none" stroke="#c5125e" stroke-width="1.3"/><path d="M3.5 6h5" stroke="#c5125e" stroke-width="1.3"/></svg></div>
  <div class="field abs" style="left:643px;width:202px">Approximate Time
    <svg width="12" height="12" viewBox="0 0 12 12"><circle cx="6" cy="6" r="5" fill="none" stroke="#c5125e" stroke-width="1.3"/><path d="M3.5 6h5" stroke="#c5125e" stroke-width="1.3"/></svg></div>
  <div class="btn-next abs">Next Steps</div>
</div>

<!-- welcome -->
<section class="welcome abs">
  <h1>Welcome To Cosmetic Surgery</h1>
  <p>Lorem ipsum dolor sit amet, consectetur adipiscing elit, sed do eiusmod tempor incididunt ut labore et dolore magna aliqua. Ut enim ad minim veniam, quis nostrud exercitation ullamco laboris nisi ut aliquip ex ea commodo consequat. Duis aute irure dolor in reprehenderit in voluptate velit esse cillum dolore eu fugiat nulla pariatur. Excepteur sint occaecat cupidatat non&nbsp; Duis aute irure dolor Duis aute irure dolor in reprehenderit</p>
</section>

<!-- services -->
<article class="service abs" style="left:99px">
  <div class="thumb" role="img" aria-label="Woman's face marked with surgical guide lines for face plastic surgery"></div>
  <span class="plus"><svg width="36" height="36" viewBox="0 0 36 36"><path d="M18 11v14M11 18h14" stroke="#fff" stroke-width="3"/></svg></span>
  <h3>Face Plastic Surgery</h3>
  <p>Lorem ipsum dolor sit amet, consec teer adipiscing. Prsent vestibulum molestie la my hendrerit. mauris hasellllus. Porta. Lorem ipsum dolor sit amet, consec</p>
  <span class="btn-more">LEARN MORE</span>
</article>
<article class="service abs" style="left:443px">
  <div class="thumb" role="img" aria-label="Abdomen marked with arrows for body plastic surgery"></div>
  <span class="plus"><svg width="36" height="36" viewBox="0 0 36 36"><path d="M18 11v14M11 18h14" stroke="#fff" stroke-width="3"/></svg></span>
  <h3>Body Plastic Surgery</h3>
  <p>Lorem ipsum dolor sit amet, consec teer adipiscing. Prsent vestibulum molestie la my hendrerit. mauris hasellllus. Porta. Lorem ipsum dolor sit amet, consec</p>
  <span class="btn-more">LEARN MORE</span>
</article>
<article class="service abs" style="left:788px">
  <div class="thumb" role="img" aria-label="Surgeon marking a patient lying down for breast plastic surgery"></div>
  <span class="plus"><svg width="36" height="36" viewBox="0 0 36 36"><path d="M18 11v14M11 18h14" stroke="#fff" stroke-width="3"/></svg></span>
  <h3>Breast Plastic Surgery</h3>
  <p>Lorem ipsum dolor sit amet, consec teer adipiscing. Prsent vestibulum molestie la my hendrerit. mauris hasellllus. Porta. Lorem ipsum dolor sit amet, consec</p>
  <span class="btn-more">LEARN MORE</span>
</article>

<!-- holiday packages -->
<section class="holiday abs" role="img" aria-label="Soft pale background with a faint woman's portrait">
  <h2>Cosmetic Surgery Holiday</h2>
  <h3>Packages in Amberlane</h3>
  <p>If you are considering medical tourism, Cosmetic Surgery Amberlane can offer you tailor made affordable cosmetic surgery holiday packages in Amberlane including accommodation and travel arrangements that suit your specific needs. We offer you top quality cosmetic surgery procedures abroad at affordable cosmetic surgery prices with dedicated aftercare. We can offer a broad range of procedures including breast surgery abroad, facial cosmetic surgery, liposuction or tummy tuck surgery. Make the right decision for your cosmetic surgery abroad with Cosmetic Surgery Amberlane and we will organise your whole stay in beautiful Amberlane, in a discreet, English-speaking, friendly and safe environment, so you can concentrate on your beauty and relax and recuperate in a stress free environment .</p>
</section>
<div class="form abs">
  <svg class="abs" style="left:200px;top:-13px" width="28" height="14" viewBox="0 0 28 14"><path d="M0 14 L14 0 L28 14" fill="#fff" stroke="#e2e2e2"/><path d="M1 14h26" stroke="#fff" stroke-width="2"/></svg>
  <div class="input focus" style="top:32px">Your Name</div>
  <div class="input" style="top:84px">E _mail</div>
  <div class="input" style="top:135px">Phone</div>
  <div class="btn-send">SEND</div>
</div>

<!-- latest blog -->
<h2 class="section-title abs" style="left:99px;top:1788px">LATEST BLOG</h2>
<div class="photo post-thumb abs" style="top:1832px" role="img" aria-label="Woman's face marked for cosmetic surgery, gloved hands nearby"></div>
<article class="post abs" style="top:1826px">
  <h4>A Guide To Cosmetic Surgery in Amberlane</h4>
  <div class="date">JAN 25, 2015</div>
  <p>Advantages of cosmetic surgery in Amberlane You can save money. Cosmetic surgery is not classified as a medical necessity in most healthcare systems, so most people have to pay for their treatment, even if their medical</p>
  <span class="btn-more">LEARN MORE</span>
</article>
<div class="photo post-thumb abs" style="top:2029px;background:linear-gradient(135deg,#8a96a3,#d9c1b1 55%,#f0e6df)" role="img" aria-label="Abdomen marked with arrows before body contouring"></div>
<article class="post abs" style="top:2023px">
  <h4>A Guide To Cosmetic Surgery in Amberlane</h4>
  <div class="date">JAN 25, 2015</div>
  <p>Advantages of cosmetic surgery in Amberlane You can save money. Cosmetic surgery is not classified as a medical necessity in most healthcare systems, so most people have to pay for their treatment, even if their medical</p>
  <span class="btn-more">LEARN MORE</span>
</article>

<!-- before & after -->
<h2 class="section-title abs" style="left:809px;top:1788px">BEFORE &amp; AFTER</h2>
<div class="photo abs" style="left:809px;top:1832px;width:292px;height:179px;background:linear-gradient(90deg,#cfe3f1,#e9d3c4 45%,#d8b9a6 60%,#dbeaf4)" role="img" aria-label="Split portrait of a woman showing before and after facial treatment"></div>
<article class="ba abs" style="top:2011px">
  <h4>A GUIDE TO COSMETIC SURGERY IN AMBERLANE</h4>
  <p>Lorem ipsum dolor sit amet, consectetur adipiscing elit, sed do eiusmod tempor incididunt ut labore et dolore magna aliqua. Ut enim ad minim veniam, quis nostrud exercitation ullamco laboris nisi</p>
  <span class="btn-more">LEARN MORE</span>
</article>

<div class="rule abs"></div>

<!-- testimonials -->
<h2 class="t-title abs">COSMETIC SURGERY TESTIMONIALS</h2>
<div class="avatar abs" style="left:100px;top:2336px" role="img" aria-label="Portrait of a smiling client"></div>
<blockquote class="quote abs" style="left:237px;top:2336px">
  <span class="mark">&ldquo;</span>I work within health myself and can honestly say Dr Maren impressed me with his polite warming maner, professionalism and amazing competence. I am absolutley over the moon with the results and just regret not getting
  <div class="who"><b>LYDIA</b> - Rhinoplasty and Breast Enlargement</div>
</blockquote>
<div class="avatar abs" style="left:638px;top:2336px" role="img" aria-label="Portrait of a smiling client"></div>
<blockquote class="quote abs" style="left:776px;top:2336px">
  <span class="mark">&ldquo;</span>I work within health myself and can honestly say Dr Maren impressed me with his polite warming maner, professionalism and amazing competence. I am absolutley over the moon with the results and just regret not getting
  <div class="who"><b>LYDIA</b> - Rhinoplasty and Breast Enlargement</div>
</blockquote>

<!-- contact band -->
<section class="contact abs">
  <span class="icon-ring" style="left:99px">
    <svg width="34" height="34" viewBox="0 0 34 34"><path d="M12 9c1 0 2 3 2 4s-2 2-1 4 3 4 5 5 2-1 3-1 4 1 4 2-1 3-3 3c-6 0-13-7-13-13 0-2 2-4 3-4z" fill="#fff"/></svg>
  </span>
  <div class="info" style="left:153px">Phone&nbsp; : +1 (555) 014-2736<br>Email&nbsp;&nbsp; : info@cosmetic-surgery-amberlane.co.uk</div>
  <span class="icon-ring" style="left:523px">
    <svg width="34" height="34" viewBox="0 0 34 34"><path d="M17 8a6 6 0 0 1 6 6c0 5-6 12-6 12s-6-7-6-12a6 6 0 0 1 6-6z" fill="#fff"/><circle cx="17" cy="14" r="2.3" fill="#c84b97"/></svg>
  </span>
  <div class="info" style="left:572px">Cosmetic Surgery Amberlane. 42 Harrowgate Lane<br>Amberlane, AL 20417</div>
  <div class="btn-quick">QUICK ENQUIRY</div>
</section>

<!-- footer -->
<footer class="footer abs">
  <h3 class="f-title" style="left:99px">AESTHETIC PLASTIC SURGERY TREATMENTS</h3>
  <div class="f-sub">Face, Body, Breast Plastic Surgery</div>
  <ul class="f-list" style="left:99px;top:90px">
    <li>Eyelid Surgery – From £950</li>
    <li>Facelift (inc neck and cheek) – £2400</li>
    <li>Rhinoplasty (inc Septoplasty) – £1800</li>
  </ul>
  <ul class="f-list" style="left:362px;top:90px">
    <li>Breast Augmentation – £1875</li>
    <li>Breast Lift – £2100</li>
    <li>Breast Reduction – £2300</li>
  </ul>
  <h3 class="f-title" style="left:612px">SOCIAL MEDIA</h3>
  <span class="social" style="left:612px" aria-label="Social profile"></span>
  <span class="social" style="left:664px" aria-label="Social profile"></span>
  <span class="social" style="left:717px" aria-label="Social profile"></span>
  <h3 class="f-title" style="left:845px">NEWSLETTER SIGN UP</h3>
  <div class="news-input"></div>
  <div class="btn-sub">SUBSCRIBE</div>
  <div class="copy">2015&nbsp; All Rights Reserved, Cosmetic Surgery Amberlane</div>
</footer>

</body>
</html>
```